Journal indexing service aimed at teachers

We are keen to redesign the appearance and functionality of lessonkite.co.nz, a site aimed at teachers.
Lessonkite provides teachers with a the ability to search for teaching resources in a printed journal series.

Clickable wireframes of the intended functionality can be seen at:
http://lessonkite.tarnpage.co.nz/wireframes
user: administrator
password: lessonkite

These wireframes are also attached here as a zip file (you'll need an Internet connection to see the images when loading them in a browser).

The redesigned site needs to be attractive and easy for users to use, and should be friendly and not too business / corporate-like.

The high majority of users will be only interested in the search functionality (which is why it is so prominent throughout the site).

We don't particularly want to continue using the current pink colouring and logo of the existing site, so please ignore these.

It also needs to be able to be responsive such that it can be used on desktop computers and tablets (though not phones).

Any design submissions should be based on treatments of
* The home page:
http://lessonkite.tarnpage.co.nz/wireframes/#/page=5AE161CA82577B2894710D933DA68252
* The search results page:
http://lessonkite.tarnpage.co.nz/wireframes/#/page=7C6A2B8FF40D5075FE250E12A37B03C5
http://lessonkite.tarnpage.co.nz/wireframes/#/page=EF9491C1CB205D41D09A0E59219E4870

We expect to have to support browsers back to IE8, though we can use polyfills to use modern web conventions in these older browsers.
Updates

Project Deadline Extended
Reason: Deadline for the designs of the Journal indexing service has been extended by another 7 days -- please let me know if anyone has any questions.

Target Market(s)

Primary school teachers

Industry/Entity Type

Business

Colors

Designer to choose colors to be used in the design.

Requirements
Must have
• Must be friendly and inviting
Should not have
• Should not be too business-like

```html
<!DOCTYPE html>
<html lang="en">
<head>
<meta charset="utf-8">
<title>Lessonkite – Search</title>
<link rel="stylesheet" href="https://fonts.googleapis.com/css2?family=Roboto:wght@400;500;700&display=swap">
<style>
:root{
  --red:#d3392b;
  --red-dark:#b92d21;
  --ink:#1d1d1d;
  --text:#333;
  --muted:#888;
  --hero:#efefef;
  --page:#fff;
  --footer:#ececec;
  --line:#dcdcdc;
  --navy:#1f3f6e;
  --poem:#5ec8f2;
  --story:#9a6ff0;
  --play:#18b84e;
  --blue-logo:#1f3a78;
}
*{box-sizing:border-box;margin:0;padding:0}
html,body{width:1050px;height:1200px;overflow:hidden}
body{font-family:'Roboto',Arial,sans-serif;color:var(--text);background:var(--page);position:relative}
.abs{position:absolute}
/* nav */
.topbar{left:0;top:0;width:1050px;height:5px;background:var(--red)}
.nav{left:0;top:5px;width:1050px;height:47px;background:#fff;box-shadow:0 2px 4px rgba(0,0,0,.08);z-index:2}
.nav a{position:absolute;top:14px;font-size:13px;color:#555;text-decoration:none;transform:translateX(-50%)}
.nav .home{left:243px;top:0;width:66px;height:54px;background:var(--red);color:#fff;border-radius:0 0 4px 4px;transform:none;text-align:center;line-height:50px;font-size:13.5px}
/* hero */
.hero{left:0;top:52px;width:1050px;height:330px;background:var(--hero);box-shadow:inset 0 -2px 3px rgba(0,0,0,.05)}
.brand{left:0;width:1050px;text-align:center}
.brand-name{top:96px;font-size:32px;font-weight:500;color:var(--red)}
.brand-sub{top:134px;font-size:10.5px;color:var(--blue-logo);line-height:13px}
.hero h1{left:0;top:174px;width:1050px;text-align:center;font-size:32px;font-weight:500;color:var(--ink)}
.hero-lead{left:0;top:219px;width:1050px;text-align:center;font-size:12px;color:var(--ink)}
.search{left:301px;top:242px;width:449px;height:32px;background:#fff;border:1px solid #c9c9c9;border-radius:2px}
.search svg{position:absolute;left:9px;top:7px}
.search span{position:absolute;left:36px;top:9px;font-size:10.5px;color:#aaa}
.radios{top:290px;font-size:12px;color:var(--red)}
.radio{position:absolute;display:flex;align-items:center;gap:7px;white-space:nowrap}
.radio i{width:10px;height:10px;border-radius:50%;background:#ddd;border:1px solid #bbb;display:block;position:relative}
.radio i.on::after{content:"";position:absolute;left:2px;top:2px;width:4px;height:4px;border-radius:50%;background:#333}
.more{top:326px;left:400px;font-size:12px;color:var(--ink);display:flex;align-items:center;gap:7px}
.btn-outline{border:1px solid #bbb;background:#fff;color:var(--red);padding:0 10px;height:29px;line-height:27px;border-radius:2px;font-size:12px}
/* sidebar */
.filters{left:179px;top:419px;width:149px;height:350px;background:var(--red);border-radius:3px;box-shadow:0 1px 3px rgba(0,0,0,.2);color:#fff}
.filters h2{font-size:14px;font-weight:500;padding:10px 10px 0;height:33px}
.filters li{list-style:none;height:28.5px;border-top:1px solid var(--red-dark);display:flex;justify-content:space-between;align-items:center;padding:0 10px 0 11px;font-size:10.5px}
.filters li b{font-weight:400;width:30px}
/* results */
.results-title{left:351px;top:419px;font-size:18px;font-weight:500;color:var(--ink)}
.count{left:572px;top:424px;font-size:12.5px;color:#555}
.print{left:741px;top:419px;width:130px;height:24px;background:var(--red);color:#fff;border-radius:2px;font-size:10.5px;font-weight:500;display:flex;align-items:center;gap:10px;padding-left:13px}
.print-note{left:741px;top:449px;width:123px;text-align:right;font-size:8.5px;color:#777}
.rule{height:1px;background:var(--line)}
.sortbar{top:480px;left:351px;font-size:10.5px;color:#888}
.select{position:absolute;top:0;height:19px;border:1px solid #ccc;background:#fff;font-size:9px;color:#555;padding:4px 7px;border-radius:2px}
.select::after{content:"";position:absolute;right:0;top:0;width:16px;height:17px;border-left:1px solid #ccc}
.select svg{position:absolute;right:4px;top:7px;z-index:1}
.pager{font-size:10.5px;color:#333;display:flex;gap:3.5px;align-items:center}
.pager .dim{color:#aaa}
/* cards */
.card{left:351px;width:519px;height:127px;background:linear-gradient(#fafafa,#f1f1f1);border:1px solid #ddd;border-radius:4px}
.cover{position:absolute;left:13px;top:10px;width:75px;height:105px}
.card h3{position:absolute;left:101px;top:8px;font-size:12.5px;font-weight:400;color:var(--red)}
.by{position:absolute;left:101px;top:24px;font-size:11px;color:var(--ink)}
.desc{position:absolute;left:101px;top:40px;font-size:9px;color:var(--ink)}
.meta{position:absolute;left:101px;top:60px;font-size:9px;color:#555;line-height:12px}
.detail{position:absolute;left:100px;top:89px;width:74px;height:20px;background:var(--red);color:#fff;font-size:9.5px;text-align:center;line-height:20px;border-radius:2px}
.tag{position:absolute;left:450px;top:10px;width:57px;height:20px;border-radius:2px;color:#fff;font-size:9.5px;text-align:center;line-height:20px}
.tag.poem{background:var(--poem)} .tag.story{background:var(--story)} .tag.play{background:var(--play)}
.pick{position:absolute;left:442px;top:89px;width:65px;height:20px;background:var(--navy);color:#fff;font-size:9.5px;border-radius:2px;display:flex;align-items:center;justify-content:center;gap:6px}
.bottom-more{left:181px;top:950px;font-size:12px;color:var(--ink)}
.bottom-more span{color:var(--red)}
/* footer */
.footer{left:0;top:1001px;width:1050px;height:199px;background:var(--footer)}
.foot-name{left:198px;top:1046px;font-size:24px;font-weight:500;color:var(--red)}
.foot-sub{left:210px;top:1078px;font-size:8px;color:var(--blue-logo);line-height:10px}
.copy{left:197px;top:1107px;font-size:10.5px;color:#555}
.copy span{color:var(--red)}
.foot-h{font-size:11.5px;color:var(--ink);font-weight:500}
.foot-line{font-size:10.5px;color:#444;display:flex;align-items:center;gap:10px}
.field{left:693px;width:177px;height:18px;background:#fff;border:1px solid #ddd;border-radius:3px;font-size:9.5px;color:#999;padding:3px 7px}
.signup{left:695px;top:1127px;width:72px;height:21px;background:var(--red);color:#fff;font-size:10.5px;border-radius:2px;text-align:center;line-height:21px}
</style>
</head>
<body>
<div class="abs topbar"></div>
<nav class="abs nav">
  <a class="home">Home</a>
  <a style="left:370px">News</a>
  <a style="left:463px">Resources</a>
  <a style="left:566px">About</a>
  <a style="left:655px">Help</a>
  <a style="left:763px">Contact Us</a>
</nav>

<section class="abs hero"></section>
<div class="abs brand brand-name">Lessonkite</div>
<div class="abs brand brand-sub">Online catalogue of the Classroom Reader<br>and other resources</div>
<h1 class="abs">Search Lessonkite</h1>
<p class="abs hero-lead">Search everything, or filter by journel items, Resources, or News Articals</p>
<div class="abs search">
  <svg width="18" height="18" viewBox="0 0 18 18"><circle cx="7.5" cy="7.5" r="6" fill="none" stroke="#999" stroke-width="1.4"/><line x1="12" y1="12" x2="16.5" y2="16.5" stroke="#999" stroke-width="1.6"/></svg>
  <span>Search Lessonkite</span>
</div>
<div class="abs radios" style="left:0;width:1050px">
  <label class="radio" style="left:376px"><i class="on"></i>All</label>
  <label class="radio" style="left:429px"><i></i>Journal items</label>
  <label class="radio" style="left:539px"><i></i>Resources</label>
  <label class="radio" style="left:630px"><i></i>News</label>
</div>
<div class="abs more">Not enough option ? <span class="btn-outline">Try our Advanced Search</span></div>

<aside class="abs filters">
  <h2>Filter Result By:</h2>
  <ul>
    <li>Level / Part<b>2,413</b></li>
    <li>Reading Level<b>817</b></li>
    <li>Curriculum<b>1,043</b></li>
    <li>Big Ideas<b>53</b></li>
    <li>Keywords<b>3,412</b></li>
    <li>Resource type<b>412</b></li>
    <li>Text type / genre<b>867</b></li>
    <li>Key competencies<b>745</b></li>
    <li>Values<b>323</b></li>
    <li>Language features<b>898</b></li>
    <li>Text scaffolds<b>32</b></li>
  </ul>
</aside>

<h2 class="abs results-title">Search Results</h2>
<div class="abs count">1-10 OF 239 Items</div>
<div class="abs print">
  <svg width="17" height="15" viewBox="0 0 17 15"><rect x="4" y="0" width="9" height="4" fill="#fff"/><rect x="0" y="4" width="17" height="7" rx="1.5" fill="#fff"/><rect x="4" y="9" width="9" height="6" fill="#fff" stroke="#d3392b" stroke-width="1"/></svg>
  Print Selections
</div>
<div class="abs print-note">6 items Selected for Printing</div>
<div class="abs rule" style="left:355px;top:467px;width:513px"></div>

<div class="abs sortbar" style="width:520px;height:20px">
  <span style="position:absolute;left:0;top:3px">Sort By</span>
  <div class="select" style="left:44px;width:74px">Relevance<svg width="7" height="4"><path d="M0 0h7L3.5 4z" fill="#333"/></svg></div>
  <span style="position:absolute;left:130px;top:3px">View</span>
  <div class="select" style="left:169px;width:48px">10<svg width="7" height="4"><path d="M0 0h7L3.5 4z" fill="#333"/></svg></div>
  <div class="pager" style="position:absolute;left:333px;top:3px"><span class="dim">&lt;&lt;&nbsp; Prev</span><span>1</span><span>2</span><span>3</span><span>4</span><span>5</span><span>6</span><span>7</span><span>8</span><span>9</span><span>10</span><span class="dim">Next &nbsp;&gt;&gt;</span></div>
</div>

<article class="abs card" style="top:514px">
  <div class="cover" role="img" aria-label="Journal cover with birds in flight, September 2011" style="background:linear-gradient(160deg,#b9a898,#8d7c6e)"></div>
  <h3>Advertising</h3>
  <div class="by">by HARTWELL, Alan</div>
  <div class="desc">This is a humorous rhyminng poem about cats and their affinity for food</div>
  <div class="meta">L3 No. 2<br>Sep 2011 48</div>
  <div class="detail">VIEW DETAIL</div>
  <div class="tag poem">POEM</div>
  <div class="pick"><svg width="11" height="11" viewBox="0 0 11 11"><path d="M4.5 6.5l2-2M3.5 5L2 6.5a2 2 0 003 3L6.5 8M7.5 6L9 4.5a2 2 0 00-3-3L4.5 3" stroke="#fff" stroke-width="1.2" fill="none"/></svg>SELECT</div>
</article>

<article class="abs card" style="top:649px">
  <div class="cover" role="img" aria-label="Journal cover illustration, 1998 issue" style="background:linear-gradient(160deg,#3a2a7a,#25185a 70%,#7a2a3a)"></div>
  <h3>Bat The Cat</h3>
  <div class="by">by KEMPTHORNE, Norman</div>
  <div class="desc">This is a humorous rhyminng poem about cats and their affinity for food</div>
  <div class="meta">L3 No. 2<br>Sep 2011 48</div>
  <div class="detail">VIEW DETAIL</div>
  <div class="tag story">STORY</div>
  <div class="pick"><svg width="11" height="11" viewBox="0 0 11 11"><path d="M4.5 6.5l2-2M3.5 5L2 6.5a2 2 0 003 3L6.5 8M7.5 6L9 4.5a2 2 0 00-3-3L4.5 3" stroke="#fff" stroke-width="1.2" fill="none"/></svg>SELECT</div>
</article>

<article class="abs card" style="top:784px">
  <div class="cover" role="img" aria-label="Colourful journal cover illustration with plants" style="background:linear-gradient(160deg,#f4e3b8,#d9a560 55%,#3f7d6a)"></div>
  <h3>The Brilliant plan: A STORY FORM TIBET</h3>
  <div class="by">by HARTWELL, Alan</div>
  <div class="desc">This is a humorous rhyminng poem about cats and their affinity for food</div>
  <div class="meta">L3 No. 2<br>Sep 2011 48</div>
  <div class="detail">VIEW DETAIL</div>
  <div class="tag play">PLAY</div>
  <div class="pick"><svg width="11" height="11" viewBox="0 0 11 11"><path d="M4.5 6.5l2-2M3.5 5L2 6.5a2 2 0 003 3L6.5 8M7.5 6L9 4.5a2 2 0 00-3-3L4.5 3" stroke="#fff" stroke-width="1.2" fill="none"/></svg>SELECT</div>
</article>

<div class="abs rule" style="left:179px;top:930px;width:692px"></div>
<div class="abs bottom-more">Not enough option ? <span>Try our Advanced Search</span></div>
<div class="abs pager" style="left:681px;top:950px"><span class="dim">&lt;&lt;&nbsp; Prev</span><span>1</span><span>2</span><span>3</span><span>4</span><span>5</span><span>6</span><span>7</span><span>8</span><span>9</span><span>10</span><span class="dim">Next &nbsp;&gt;&gt;</span></div>

<footer class="abs footer"></footer>
<div class="abs foot-name">Lessonkite</div>
<div class="abs foot-sub">Online catalogue of the Classroom Reader<br>and other resources</div>
<div class="abs copy"><span>Lessonkite</span> © 2014 | Privacy Policy</div>

<div class="abs foot-h" style="left:450px;top:1040px">Contact Us</div>
<div class="abs foot-line" style="left:447px;top:1070px">
  <svg width="16" height="11" viewBox="0 0 16 11"><rect x=".5" y=".5" width="15" height="10" fill="none" stroke="#999"/><path d="M.5 .5l7.5 6 7.5-6" fill="none" stroke="#999"/></svg>info@lessonkite.co.nz</div>
<div class="abs foot-line" style="left:447px;top:1096px">
  <svg width="16" height="16" viewBox="0 0 16 16"><path d="M3 1l3 3-1.5 2a9 9 0 005 5L11.5 9.5l3 3-2 2C6 14 2 10 1 3.5z" fill="none" stroke="#999"/></svg>021 555 0142</div>
<div class="abs foot-line" style="left:446px;top:1122px">Contact: Lessonkite Customer Services</div>

<div class="abs foot-h" style="left:693px;top:1040px">Our Newsletter</div>
<div class="abs field" style="top:1072px">Name....</div>
<div class="abs field" style="top:1100px">Email....</div>
<div class="abs signup">Sign up now</div>
</body>
</html>
```